Business Card Design for a Handbags business

We are modernising our handbags website (see attached file for new front page) and are in need of a modern business card and a related design we can use on a small marquee at the markets, on letterhead, emails etc.

As the leather handbags we mostly import are from Italy, we want a smart modern European feel to the design. We are currently thinking about changing the name of the business from Meadowlark Handbags (see www.meadowlarkhandbags.com.au) to Vantera Handbags. Also open to other suggestions you may have that communicates the European influence and quality.

Target Market(s)

25-65 year old women (and some men)

Industry/Entity Type

Business

Contact Information for Business Card

Single or double sided - whichever creates more of an impact

Font styles to use
Serif
Sans Serif

Requirements
Must have
• Clean crisp look, slightly Italian or European look and feel to reflect where the handbags are imported from
Nice to have
• open to ideas

```html
<!DOCTYPE html>
<html lang="en">
<head>
<meta charset="utf-8">
<title>Vantera Handbags – Business Card</title>
<link href="https://fonts.googleapis.com/css2?family=Raleway:wght@500;600&family=Source+Sans+3:ital,wght@0,400;1,400&family=Parisienne&display=swap" rel="stylesheet">
<style>
  :root {
    --stage: #000000;
    --card-front: #f3f3f3;
    --card-back: #ffffff;
    --magenta: #cc12c6;
    --ink: #1a1a1a;
    --rule: #d4d4d4;
    --photo-light: #e9e9ea;
    --photo-mid: #c9bfb6;
    --photo-dark: #1b1b1d;
  }
  * { margin: 0; padding: 0; box-sizing: border-box; }
  html, body {
    width: 1200px; height: 900px; overflow: hidden;
    background: var(--stage);
  }
  .stage { position: relative; width: 1200px; height: 900px; }

  .card {
    position: absolute; top: 200px; width: 310px; height: 502px; overflow: hidden;
  }
  .card--front {
    left: 304px; background: var(--card-front);
    border-radius: 62px 0 62px 0;
  }
  .card--back {
    left: 641px; width: 309px; background: var(--card-back);
    border-radius: 0 62px 0 62px;
  }

  .brand { position: absolute; text-align: right; }
  .brand__name {
    display: block;
    font-family: "Raleway", sans-serif; font-weight: 500;
    color: var(--magenta); line-height: 1; letter-spacing: 1px;
  }
  .brand__tagline {
    display: block;
    font-family: "Raleway", sans-serif; font-weight: 600;
    color: var(--ink); line-height: 1;
  }
  .card--front .brand { right: 36px; top: 52px; }
  .card--front .brand__name { font-size: 62px; }
  .card--front .brand__tagline { font-size: 17.5px; margin-top: 12px; }

  .contact { position: absolute; left: 22px; top: 272px; }
  .contact__person {
    font-family: "Parisienne", cursive; font-size: 27px;
    color: var(--magenta); line-height: 1;
  }
  .contact__list { list-style: none; margin-top: 16px; }
  .contact__item {
    display: flex; align-items: center; gap: 6px;
    font-family: "Source Sans 3", sans-serif; font-size: 14.5px; color: var(--ink);
    height: 20px;
  }
  .contact__item--place { margin-top: 12px; }
  .contact__item svg { width: 11px; height: 11px; fill: var(--magenta); flex: none; }

  .divider {
    position: absolute; left: 22px; top: 407px; width: 154px; height: 1px;
    background: var(--rule);
  }
  .slogan {
    position: absolute; left: 22px; top: 425px;
    font-family: "Source Sans 3", sans-serif; font-style: italic;
    font-size: 17.5px; line-height: 24px; color: var(--ink);
  }

  .photo {
    position: absolute; left: 0; top: 0; width: 170px; height: 502px;
    background: linear-gradient(180deg, var(--photo-light) 0%, var(--photo-mid) 35%, #e2dcd6 55%, var(--photo-dark) 68%, var(--photo-dark) 100%);
  }
  .card--back .brand { right: 20px; top: 230px; }
  .card--back .brand__name { font-size: 44px; }
  .card--back .brand__tagline { font-size: 13px; margin-top: 8px; }
</style>
</head>
<body>
<main class="stage">
  <section class="card card--front">
    <div class="brand">
      <span class="brand__name">Vantera</span>
      <span class="brand__tagline">Handbags &amp; Accessories</span>
    </div>
    <div class="contact">
      <p class="contact__person">Juliette Marlow</p>
      <ul class="contact__list">
        <li class="contact__item">
          <svg viewBox="0 0 24 24" aria-hidden="true"><path d="M6.6 10.8a15.1 15.1 0 0 0 6.6 6.6l2.2-2.2a1 1 0 0 1 1-.25 11.4 11.4 0 0 0 3.6.57 1 1 0 0 1 1 1V20a1 1 0 0 1-1 1A17 17 0 0 1 3 4a1 1 0 0 1 1-1h3.5a1 1 0 0 1 1 1c0 1.25.2 2.45.57 3.57a1 1 0 0 1-.25 1z"/></svg>
          0412 555 019
        </li>
        <li class="contact__item">
          <svg viewBox="0 0 24 24" aria-hidden="true"><path d="M12 2a10 10 0 1 0 0 20 10 10 0 0 0 0-20zm6.9 6h-3a15.6 15.6 0 0 0-1.4-3.6A8 8 0 0 1 18.9 8zM12 4c.8 1.2 1.5 2.5 1.9 4h-3.8c.4-1.5 1.1-2.8 1.9-4zM4.3 14a8 8 0 0 1 0-4h3.4a16 16 0 0 0 0 4zm.8 2h3a15.6 15.6 0 0 0 1.4 3.6A8 8 0 0 1 5.1 16zM8 8H5.1a8 8 0 0 1 4.3-3.6A15.6 15.6 0 0 0 8 8zm4 12c-.8-1.2-1.5-2.5-1.9-4h3.8c-.4 1.5-1.1 2.8-1.9 4zm2.3-6H9.7a14.7 14.7 0 0 1 0-4h4.6a14.7 14.7 0 0 1 0 4zm.3 5.6A15.6 15.6 0 0 0 16 16h3a8 8 0 0 1-4.4 3.6zM16.3 14a16 16 0 0 0 0-4h3.4a8 8 0 0 1 0 4z"/></svg>
          www.meadowlarkhandbags.com.au
        </li>
        <li class="contact__item contact__item--place">
          <svg viewBox="0 0 24 24" aria-hidden="true"><path d="M12 2a7 7 0 0 0-7 7c0 5.2 7 13 7 13s7-7.8 7-13a7 7 0 0 0-7-7zm0 9.5A2.5 2.5 0 1 1 12 6.5a2.5 2.5 0 0 1 0 5z"/></svg>
          Brisbane
        </li>
      </ul>
    </div>
    <div class="divider"></div>
    <p class="slogan">Italian leather handbags<br>at affordable prices</p>
  </section>

  <section class="card card--back">
    <div class="photo" role="img" aria-label="Fashion photo of a woman in sunglasses carrying a black leather handbag"></div>
    <div class="brand">
      <span class="brand__name">Vantera</span>
      <span class="brand__tagline">Handbags &amp; Accessories</span>
    </div>
  </section>
</main>
</body>
</html>
```